Zertifikat-Design für Bildungsträger im Bereich der Erwachsenenbildung
Zielgruppe
Talwerk Akademie - Zertifizierter Bildungsträger im Bereich der Erwachsenenbildung. Überwiegend Mitarbeiter in Unternehmen.
Aufgabenstellung
'Erstelle ein hochwertiges, modernes und exklusiv wirkendes Zertifikat für die Talwerk Akademie. Das Design soll professionell, minimalistisch und zugleich edel sein. Ziel ist es, ein Dokument zu gestalten, das den Eindruck vermittelt: 'Das ist das einzige und beste Zertifikat in der ganzen verdammten Welt.'
Das Zertifikat soll im Querformat (idealerweise DIN A4 horizontal) gestaltet werden. Der Inhalt soll zweisprachig (Deutsch und Englisch) dargestellt werden, klar gegliedert und typografisch hochwertig aufgebaut. Alle Inhalte sollten mittig ausgerichtet sein, mit gut erkennbarer visueller Hierarchie.
Der Haupttext lautet wie folgt:
'Talwerk Akademie gratuliert 'Name / Platzhalter' zum erfolgreichen Abschluss des Kurses 'Platzhalter' Datum, Unterschrift (siehe unten)
+englisch
'Talwerk Akademie hereby certifies that [Name of Participant / Placeholder] has successfully participated on 'date'.
Darunter sollen zwei stilisierte Unterschriften platziert werden – gerne von Hand gezeichnet oder elegant typografisch umgesetzt. Die Beschriftung unter den Unterschriften lautet: 'Leitung Talwerk Akademie'.
Ein zentrales Element ist das Hologramm. Muster das gelieferte Bild 'Hologramm.png'. Es muss deutlich sichtbar und hochwertig integriert werden. Die Aufschrift 'Talwerk' im Hologramm muss klar erkennbar sein. Idealer Platz wäre unten links oder rechts, eventuell mit einer leichten 3D-Anmutung oder Glanzeffekt.
Das gesamte Design muss der Corporate Identity der Talwerk Akademie entsprechen. Die verwendeten Farben sind: Hauptfarbe Dunkelblau (RGB 14, 32, 62), ergänzt durch Hellblau (RGB 241, 245, 250), ein zusätzliches Blau (RGB 65, 111, 174), Pink (RGB 140, 130, 227), Dunkellila (RGB 169, 97, 161), sowie Gelb (RGB 248, 216, 73) und Orange (RGB 220, 121, 70) für gezielte Akzente.
Als Schriftart ist ausschließlich Roboto zu verwenden. Der Name des Teilnehmers soll besonders hervorgehoben werden (z...

```html
<!DOCTYPE html>
<html lang="de">
<head>
<meta charset="utf-8">
<title>Zertifikat – Talwerk Akademie</title>
<link href="https://fonts.googleapis.com/css2?family=Roboto:ital,wght@0,400;0,500;0,700;0,900;1,400;1,700&display=swap" rel="stylesheet">
<style>
  :root {
    --navy: #0e203e;
    --paper: #f1f5fa;
    --blue: #416fae;
    --blue-soft: #8fa9cf;
    --silver-light: #f4f5f7;
    --silver-dark: #8c9099;
  }
  * { margin: 0; padding: 0; box-sizing: border-box; }
  html, body { width: 1200px; height: 848px; overflow: hidden; background: var(--paper); }
  body { font-family: 'Roboto', sans-serif; color: var(--navy); }
  .certificate { position: relative; width: 1200px; height: 848px; background: var(--paper); }
  .frame { position: absolute; inset: 0; }
  .corner-ornament {
    position: absolute; width: 104px; height: 104px;
    background: radial-gradient(circle at center, rgba(65,111,174,0.45), rgba(14,32,62,0.15) 70%, transparent 72%);
  }
  .corner-ornament.top-left { top: 6px; left: 6px; }
  .corner-ornament.top-right { top: 6px; right: 6px; }
  .corner-ornament.bottom-left { bottom: 6px; left: 6px; }
  .corner-ornament.bottom-right { bottom: 6px; right: 6px; }
  .content { position: absolute; inset: 0; text-align: center; }
  .title { position: absolute; top: 82px; width: 100%; font-size: 90px; font-weight: 900; letter-spacing: 3px; line-height: 1; }
  .title-en { position: absolute; top: 182px; width: 100%; font-size: 30px; font-weight: 700; font-style: italic; letter-spacing: 5px; color: var(--blue); }
  .congrats { position: absolute; top: 267px; width: 100%; font-size: 30px; font-weight: 700; letter-spacing: 0.5px; }
  .congrats-en { position: absolute; top: 304px; width: 100%; font-size: 24px; font-style: italic; color: var(--blue); }
  .participant { position: absolute; top: 346px; width: 100%; font-size: 66px; font-weight: 900; letter-spacing: 1.5px; line-height: 1; }
  .course { position: absolute; top: 452px; width: 100%; font-size: 22px; font-weight: 500; line-height: 28px; }
  .course-en { position: absolute; top: 524px; width: 100%; font-size: 24px; font-style: italic; color: var(--blue); }
  .seal { position: absolute; left: 530px; top: 598px; width: 140px; height: 200px; }
  .signature { position: absolute; top: 732px; width: 318px; border-top: 1.5px solid var(--blue-soft); padding-top: 10px; font-size: 23px; font-weight: 500; text-align: center; }
  .signature.left { left: 142px; }
  .signature.right { left: 742px; }
</style>
</head>
<body>
<div class="certificate">
  <svg class="frame" width="1200" height="848" viewBox="0 0 1200 848" aria-hidden="true">
    <polygon points="40,12 1160,12 1188,40 1188,808 1160,836 40,836 12,808 12,40" fill="none" stroke="var(--blue)" stroke-width="2"/>
    <polygon points="62,24 1138,24 1176,62 1176,786 1138,824 62,824 24,786 24,62" fill="none" stroke="var(--navy)" stroke-width="2"/>
    <polygon points="70,32 1130,32 1168,70 1168,778 1130,816 70,816 32,778 32,70" fill="none" stroke="var(--navy)" stroke-width="1.5" stroke-dasharray="2 3"/>
  </svg>
  <div class="corner-ornament top-left" role="img" aria-label="Verschnörkeltes Eckornament"></div>
  <div class="corner-ornament top-right" role="img" aria-label="Verschnörkeltes Eckornament"></div>
  <div class="corner-ornament bottom-left" role="img" aria-label="Verschnörkeltes Eckornament"></div>
  <div class="corner-ornament bottom-right" role="img" aria-label="Verschnörkeltes Eckornament"></div>

  <div class="content">
    <h1 class="title">ZERTIFIKAT</h1>
    <p class="title-en">CERTIFICATE</p>
    <p class="congrats">TALWERK AKADEMIE GRATULIERT</p>
    <p class="congrats-en">Talwerk Akademie hereby certifies that</p>
    <p class="participant">PLATZHALTER'</p>
    <p class="course">zum erfolgreichen Abschluss des Kurses 'Platzhalter' Datum,<br>Unterschrift (siehe unten)</p>
    <p class="course-en">has successfully participated on 'date'</p>
  </div>

  <svg class="seal" viewBox="0 0 140 200" role="img" aria-label="Silbernes Hologramm-Siegel">
    <defs>
      <radialGradient id="silver" cx="40%" cy="35%" r="70%">
        <stop offset="0" stop-color="var(--silver-light)"/>
        <stop offset="1" stop-color="var(--silver-dark)"/>
      </radialGradient>
    </defs>
    <circle cx="70" cy="68" r="66" fill="url(#silver)"/>
  </svg>

  <div class="signature left">Leitung Talwerk Akademie</div>
  <div class="signature right">Leitung Talwerk Akademie</div>
</div>
</body>
</html>
```